Gold Award for Hygiene Excellence

We are providing food safety consultancy to restaurant business in the uk. We would like to prepare an award sticker for business that work with us to get sticker award if they got 5 star hygiene rating consecutively in the their last 3 inspections. Normally, they display hygiene scores that are green color on their shop's window. So it should be catchy color for people easily detect the award. Size A5

```html
<!DOCTYPE html>
<html lang="en">
<head>
<meta charset="utf-8">
<title>Gold Award for Hygiene Excellence</title>
<link rel="stylesheet" href="https://fonts.googleapis.com/css2?family=Jost:wght@400;500&display=swap">
<style>
  :root {
    --bg: #e9eaec;
    --black: #231f20;
    --gold: #fbb400;
    --white: #f7f7f7;
  }
  * { box-sizing: border-box; margin: 0; padding: 0; }
  html, body {
    width: 1200px;
    height: 900px;
    overflow: hidden;
    background: var(--bg);
    font-family: "Jost", "Futura", sans-serif;
  }
  .award-sticker {
    position: absolute;
    left: 80px;
    top: 70px;
    width: 1040px;
    height: 760px;
    border-radius: 18px;
    overflow: hidden;
    display: flex;
    flex-direction: column;
    box-shadow: 0 6px 18px rgba(0,0,0,.18);
  }
  .award-title {
    height: 410px;
    background: var(--black);
    color: var(--gold);
    display: flex;
    flex-direction: column;
    align-items: center;
    justify-content: center;
    padding-top: 10px;
  }
  .award-title__main {
    font-size: 262px;
    font-weight: 400;
    line-height: .86;
    letter-spacing: 14px;
    margin-right: -14px;
  }
  .award-title__sub {
    font-size: 124px;
    font-weight: 400;
    line-height: 1;
    letter-spacing: 10px;
    margin-right: -10px;
    margin-top: 8px;
  }
  .award-strap {
    height: 130px;
    background: var(--white);
    color: var(--gold);
    display: flex;
    align-items: center;
    justify-content: center;
    font-size: 67px;
    font-weight: 400;
    letter-spacing: 4px;
  }
  .award-footer {
    flex: 1;
    background: var(--gold);
    position: relative;
  }
  .award-footer__note {
    position: absolute;
    left: 42px;
    top: 78px;
    font-size: 22px;
    line-height: 1.2;
    color: var(--black);
    text-transform: uppercase;
    font-weight: 400;
  }
  .rating-scores {
    position: absolute;
    left: 340px;
    top: 48px;
    display: flex;
    gap: 6px;
  }
  .rating-score {
    width: 136px;
    height: 136px;
    border-radius: 50%;
    background: var(--black);
    color: var(--gold);
    font-size: 100px;
    font-weight: 400;
    display: flex;
    align-items: center;
    justify-content: center;
    line-height: 1;
  }
  .advisor-name {
    position: absolute;
    left: 780px;
    right: 0;
    top: 62px;
    height: 108px;
    background: var(--white);
    display: flex;
    align-items: center;
    justify-content: center;
    color: var(--black);
    font-size: 30px;
    font-weight: 400;
    letter-spacing: 0;
  }
</style>
</head>
<body>
  <main class="award-sticker">
    <header class="award-title">
      <h1 class="award-title__main">GOLD</h1>
      <p class="award-title__sub">AWARD</p>
    </header>
    <p class="award-strap">FOR HYGIENE EXCELLENCE</p>
    <section class="award-footer">
      <p class="award-footer__note">This award has<br>been given for<br>3 consecutive<br>5 star hygiene score</p>
      <div class="rating-scores">
        <span class="rating-score">5</span>
        <span class="rating-score">5</span>
        <span class="rating-score">5</span>
      </div>
      <p class="advisor-name">Halden Advisory</p>
    </section>
  </main>
</body>
</html>
```